" Precisamos de uma logomarca e cartao de visitas, para uma nova empresa de investimentos, sediada em Sao Paulo, chamada TKRP Investimentos. A empresa é uma gestora de Fundos de Private Equity que atua de forma ampla no mercado imobiliário, adquirindo e desenvolvendo ativos nos segmentos de shopping centers, galpoes logísticos e industriais, edifícios comerciais, loteamentos residenciais, hotéis, entre outros. "

```html
<!DOCTYPE html>
<html lang="pt-BR">
<head>
<meta charset="utf-8">
<title>TKRP Investimentos — Cartões de visita</title>
<link href="https://fonts.googleapis.com/css2?family=Lato:wght@400;700&display=swap" rel="stylesheet">
<style>
  :root {
    --bg: #e9e7e4;
    --navy: #1c1b5c;
    --brand-blue: #2a4d9c;
    --paper: #ffffff;
    --ink: #3a3a3a;
    --rule: #b9bcc6;
    --shadow: rgba(0,0,0,0.18);
  }
  * { margin: 0; padding: 0; box-sizing: border-box; }
  html, body { width: 1200px; height: 1200px; overflow: hidden; }
  body {
    background: var(--bg);
    font-family: "Lato", sans-serif;
    color: var(--ink);
    position: relative;
  }
  .card {
    position: absolute;
    background: var(--paper);
    box-shadow: 0 8px 22px var(--shadow);
    overflow: hidden;
  }
  .card--back {
    left: 125px; top: 262px; width: 588px; height: 326px;
    background: var(--navy);
    display: flex; align-items: center; justify-content: center;
  }
  .card--back .website {
    color: #fff; font-size: 19px; letter-spacing: 0.2px;
    transform: translateX(-20px);
  }
  .website strong { font-weight: 700; }
  .card--front { left: 125px; top: 607px; width: 588px; height: 329px; }
  .card--vertical { left: 746px; top: 307px; width: 262px; height: 586px; }

  .brand {
    position: absolute;
    font-family: "Lato", sans-serif;
    font-weight: 700;
    color: var(--brand-blue);
    display: flex; flex-direction: column; align-items: center;
    text-align: center; line-height: 1.15;
    white-space: nowrap;
  }
  .brand .dot {
    width: 18px; height: 18px; border-radius: 50%;
    background: var(--brand-blue);
    margin-bottom: 12px;
  }
  .card--front .brand { left: 52px; width: 200px; top: 102px; font-size: 26px; }
  .card--vertical .brand { left: 0; right: 0; top: 98px; font-size: 26px; }

  .contact { position: absolute; }
  .card--front .contact { left: 300px; top: 118px; width: 288px; }
  .card--vertical .contact { left: 22px; top: 372px; width: 240px; }
  .contact .name { font-weight: 700; font-size: 20px; color: #333; margin-bottom: 4px; }
  .card--vertical .contact .name { font-size: 19px; }
  .contact .email {
    font-size: 11px; display: flex; align-items: center; gap: 6px;
    padding-bottom: 8px; border-bottom: 1px solid var(--rule); margin-bottom: 10px;
  }
  .email strong { font-weight: 700; }
  .contact .line { font-size: 12px; display: flex; gap: 8px; line-height: 1.55; }
  .card--vertical .contact .line { font-size: 11px; }
  .line .icon { width: 12px; flex: none; padding-top: 3px; }
  .line.phone { font-weight: 700; margin-top: 2px; }
  .address-text { display: block; }
  svg.icon-svg { display: block; fill: #333; }
</style>
</head>
<body>

  <section class="card card--back">
    <p class="website">www.<strong>tkrpinvestimentos</strong>.com.br</p>
  </section>

  <section class="card card--front">
    <div class="brand"><span class="dot"></span><span>TKRP</span><span>Investimentos</span></div>
    <div class="contact">
      <p class="name">Nome Sobrenome</p>
      <p class="email">
        <svg class="icon-svg" width="12" height="9" viewBox="0 0 12 9"><rect x="0" y="0" width="12" height="9" rx="1"/><path d="M1 1 L6 5 L11 1" stroke="#fff" stroke-width="1" fill="none"/></svg>
        <span><strong>nome</strong>@tkrpinvestimentos.com.br</span>
      </p>
      <p class="line">
        <span class="icon"><svg class="icon-svg" width="10" height="13" viewBox="0 0 10 13"><path d="M5 0a5 5 0 0 1 5 5c0 3.5-5 8-5 8S0 8.5 0 5a5 5 0 0 1 5-5z"/><circle cx="5" cy="5" r="2" fill="#fff"/></svg></span>
        <span class="address-text">R. Campo Verde, 480 - Cj. 31/32<br>CEP: 01452-000 - Cidade - UF</span>
      </p>
      <p class="line phone">
        <span class="icon"><svg class="icon-svg" width="12" height="12" viewBox="0 0 12 12"><circle cx="6" cy="6" r="5.5" fill="none" stroke="#333"/><path d="M4 3.2 L5 3 L5.6 4.6 L5 5.2 Q5.6 6.5 6.8 7 L7.4 6.4 L9 7 L8.8 8 Q6.5 8.6 4.7 6.8 Q3.2 5 4 3.2z"/></svg></span>
        <span>(00) 3210.4477 / 3210.0000</span>
      </p>
    </div>
  </section>

  <section class="card card--vertical">
    <div class="brand"><span class="dot"></span><span>TKRP</span><span>Investimentos</span></div>
    <div class="contact">
      <p class="name">Nome Sobrenome</p>
      <p class="email">
        <svg class="icon-svg" width="12" height="9" viewBox="0 0 12 9"><rect x="0" y="0" width="12" height="9" rx="1"/><path d="M1 1 L6 5 L11 1" stroke="#fff" stroke-width="1" fill="none"/></svg>
        <span><strong>nome</strong>@tkrpinvestimentos.com.br</span>
      </p>
      <p class="line">
        <span class="icon"><svg class="icon-svg" width="10" height="13" viewBox="0 0 10 13"><path d="M5 0a5 5 0 0 1 5 5c0 3.5-5 8-5 8S0 8.5 0 5a5 5 0 0 1 5-5z"/><circle cx="5" cy="5" r="2" fill="#fff"/></svg></span>
        <span class="address-text">R. Campo Verde, 480 - Cj. 31/32<br>CEP: 01452-000 - Cidade - UF</span>
      </p>
      <p class="line phone">
        <span class="icon"><svg class="icon-svg" width="12" height="12" viewBox="0 0 12 12"><circle cx="6" cy="6" r="5.5" fill="none" stroke="#333"/><path d="M4 3.2 L5 3 L5.6 4.6 L5 5.2 Q5.6 6.5 6.8 7 L7.4 6.4 L9 7 L8.8 8 Q6.5 8.6 4.7 6.8 Q3.2 5 4 3.2z"/></svg></span>
        <span>(00) 3210.4477 / 3210.0000</span>
      </p>
    </div>
  </section>

</body>
</html>
```